Strong Pulse, Clear Mind Poster for American Indian Older Adults

We need am 11" x 17" poster designed for a health outreach project designed to reach older U.S. American Indians. The materials developed through this project will be distributed to American Indian and Alaska Native tribes, communities and tribal-serving organizations across the U.S. (more than 500 different tribes). If we find a successful design we will work with that designer to produce at least one other item we need design work for using the same look/feel and maybe other materials for this project. (more work!). The poster will include a set of facts (bulleted list on the attached document) that we would like presented in an "infographic" style. The design must be reflective of the American Indian culture and designed with older adults (65 and older) in mind. Imagery plays a strong role in the American Indian culture in the U.S. images of the heart, water, feathers, circle of life, etc. If you use photos of people they must include older adults and they must be American Indian (Native American). We prefer deep earth tones for the color scheme. The design must take into account design principles for older adults: 1. Try not to put colored font on colored background 2. Ensure high contrast for text 3. Font style should be sans serif, not cursive,decorative or heavily stylized because it is harder to read 4. Avoid using all caps 5. Don't print sideways or on top of images, shaded, backgrounds, etc. 6. All images should related specifically to the content of the text and be culturally appropriate for both older adults and American Indians. The final design should be easy to read and appeal to older American Indian adults. We need to incorporate three logos on the poster towards the bottom they should not be the center/focus of the poster. We also need to include a statement about who produced the materials- that can be very small below the logos at the bottom of the poster. We've attached the text for the poster and three logo files (note one is solid blue- we will finalize that after the document design is selected but need a placeholder for that logo.

Target Market(s)

Older adult (65 and older) American Indian and Alaska Natives and their family members in tribes, communities and tribal-serving organizations across the US

Font styles to use
Sans Serif

Requirements
Must have
• Must adhere to good design principles for older adults (listed in project description)
• Must feature culturally appropriate/targeted imagery and design look and feel

```html
<!DOCTYPE html>
<html lang="en">
<head>
<meta charset="utf-8">
<title>Strong Pulse, Clear Mind</title>
<link rel="stylesheet" href="https://fonts.googleapis.com/css2?family=Roboto:wght@900&family=Source+Sans+3:wght@400;600;700&family=Open+Sans:ital,wght@1,700&display=swap">
<style>
  :root {
    --cream: #fcebdb;
    --cream-light: #fff6ee;
    --brown: #47291f;
    --crimson: #8c1a2c;
    --crimson-deep: #7d1424;
    --water-top: #e9ddd6;
    --water-mid: #cfc3bf;
    --photo-warm: #e6c9b4;
    --photo-rose: #b4688f;
    --photo-skin: #9a6a55;
    --white: #ffffff;
    --logo-green: #3d8a47;
  }
  * { margin: 0; padding: 0; box-sizing: border-box; }
  html, body { width: 1200px; height: 775px; overflow: hidden; background: var(--cream); }
  .poster {
    position: relative; width: 1200px; height: 775px; overflow: hidden;
    background: linear-gradient(180deg, var(--cream) 0%, var(--cream) 70%, var(--cream-light) 100%);
    font-family: "Source Sans 3", Arial, sans-serif; color: var(--brown);
  }
  .elder-portrait {
    position: absolute; right: 0; top: 0; width: 470px; height: 575px;
    background:
      radial-gradient(ellipse 150px 190px at 66% 35%, var(--photo-skin) 0%, rgba(154,106,85,0.6) 55%, rgba(154,106,85,0) 100%),
      radial-gradient(ellipse 230px 180px at 70% 95%, var(--photo-rose) 0%, rgba(180,104,143,0.5) 60%, rgba(180,104,143,0) 100%),
      linear-gradient(90deg, rgba(252,235,219,1) 0%, rgba(230,201,180,0.6) 35%, var(--photo-warm) 100%);
    -webkit-mask-image: linear-gradient(90deg, transparent 0%, #000 30%);
            mask-image: linear-gradient(90deg, transparent 0%, #000 30%);
  }
  .title {
    position: absolute; left: 30px; top: 30px;
    font-family: "Roboto", Arial, sans-serif; font-weight: 900;
    font-size: 87px; line-height: 84px; letter-spacing: -0.5px; color: var(--brown);
  }
  .tagline {
    position: absolute; left: 30px; top: 222px;
    font-weight: 700; font-size: 27px; line-height: 37px; color: var(--crimson);
  }
  .people-icon { position: absolute; left: 26px; top: 384px; width: 140px; height: 166px; }
  .stat-figure {
    position: absolute; left: 226px; top: 388px;
    font-family: "Roboto", Arial, sans-serif; font-weight: 900;
    font-size: 78px; line-height: 78px; color: var(--crimson);
    border-bottom: 3px solid var(--crimson); padding-bottom: 2px; width: 258px;
  }
  .stat-caption {
    position: absolute; left: 228px; top: 480px;
    font-size: 36px; line-height: 38px; font-weight: 400; color: var(--brown);
  }
  .water-band {
    position: absolute; left: 0; top: 566px; width: 1200px; height: 90px;
    background: linear-gradient(180deg, var(--water-top) 0%, var(--water-mid) 45%, var(--cream-light) 100%);
  }
  .pulse-line { position: absolute; left: 0; top: 510px; width: 1200px; height: 90px; }
  .call-to-action {
    position: absolute; left: 27px; top: 648px; width: 720px; height: 90px;
    background: var(--crimson-deep); border-radius: 45px;
    display: flex; align-items: center; justify-content: center; text-align: center;
    font-family: "Open Sans", Arial, sans-serif; font-style: italic; font-weight: 700;
    font-size: 25px; line-height: 33px; color: var(--white);
  }
  .partners {
    position: absolute; left: 878px; top: 668px; display: flex; align-items: center; gap: 22px;
  }
  .partner-name { font-weight: 700; font-size: 17px; color: var(--brown); line-height: 1; }
  .partner-name--council { border-bottom: 2px solid var(--logo-green); padding-bottom: 3px; font-size: 14px; }
  .credit {
    position: absolute; left: 880px; top: 724px; width: 290px;
    font-size: 6px; line-height: 7.5px; font-weight: 600; color: var(--brown);
  }
</style>
</head>
<body>
<main class="poster">
  <div class="elder-portrait" role="img" aria-label="Photograph of an American Indian elder woman in a magenta blouse, set over a soft woven geometric pattern"></div>

  <h1 class="title">Strong Pulse,<br>Clear Mind ...</h1>
  <p class="tagline">The River of Life Flows<br>Through the Heart,<br>Protecting the Mind and Body</p>

  <svg class="people-icon" viewBox="0 0 140 166" aria-hidden="true">
    <defs>
      <g id="person">
        <circle cx="0" cy="0" r="6"/>
        <rect x="-8" y="8" width="16" height="22" rx="3"/>
        <rect x="-7" y="28" width="6" height="20"/>
        <rect x="1" y="28" width="6" height="20"/>
      </g>
    </defs>
    <use href="#person" x="70" y="6" fill="var(--brown)"/>
    <g fill="var(--crimson)">
      <use href="#person" x="52" y="44"/><use href="#person" x="88" y="44"/>
      <use href="#person" x="34" y="82"/><use href="#person" x="70" y="82"/><use href="#person" x="106" y="82"/>
      <use href="#person" x="14" y="118"/><use href="#person" x="52" y="118"/><use href="#person" x="88" y="118"/><use href="#person" x="126" y="118"/>
    </g>
  </svg>

  <div class="stat-figure">1 in 10</div>
  <p class="stat-caption">People age 65 and older<br>has Alzheimer’s</p>

  <div class="water-band" role="img" aria-label="Calm river water stretching to the horizon"></div>

  <svg class="pulse-line" viewBox="0 0 1200 90" aria-hidden="true">
    <path d="M0 56 H770 L777 40 L783 70 L790 30 L797 56 H820 M880 56 H882 L888 46 L894 66 L900 56 H910 M934 56 H940 L946 36 L952 76 L958 56 H1178"
          fill="none" stroke="var(--crimson)" stroke-width="1.8"/>
    <ellipse cx="850" cy="38" rx="26" ry="20" fill="var(--crimson)" role="img" aria-label="Brain icon"/>
    <path d="M848 56 L850 74 L852 56" fill="none" stroke="var(--crimson)" stroke-width="2"/>
    <path d="M922 60 C912 52 908 44 914 40 C919 36 922 42 922 44 C922 42 925 36 930 40 C936 44 932 52 922 60 Z"
          fill="none" stroke="var(--crimson)" stroke-width="1.8"/>
  </svg>

  <p class="call-to-action">Make an appointment with your doctor today to<br>talk about how to keep your mind and heart healthy.</p>

  <div class="partners">
    <span class="partner-name">Kestrel Health</span>
    <span class="partner-name partner-name--council">Circle of Elders Council</span>
  </div>
  <p class="credit">This poster was made possible by a community health grant awarded to tribal partners. Its contents are solely the responsibility of the authors and do not necessarily represent the official views of the funding agency or its partners.</p>
</main>
</body>
</html>
```